Copper Gavel Auctions business card design with existing logo

Looking for a sleek and sexy design using our current logo

Contact Information for Business Card

Name, address, email, phone, website. Gregory Vandale 482 Thornbury Road Suite 214C Marlow Falls NY 14583 Coppergavelbids.net (555)482-6613

```html
<!DOCTYPE html>
<html lang="en">
<head>
<meta charset="utf-8">
<title>Copper Gavel Auctions – Business Card</title>
<link rel="stylesheet" href="https://fonts.googleapis.com/css2?family=Saira:wght@400;600;800&display=swap">
<style>
  :root {
    --bg: #a9b9b3;
    --navy: #1f4a80;
    --navy-deep: #163d70;
    --red: #d52b36;
    --white: #ffffff;
    --faint: rgba(255,255,255,0.07);
  }
  * { margin: 0; padding: 0; box-sizing: border-box; }
  html, body {
    width: 1200px; height: 1000px; overflow: hidden;
    background: var(--bg);
    font-family: "Saira", sans-serif;
  }
  .canvas { position: relative; width: 1200px; height: 1000px; }

  .card {
    position: absolute;
    width: 540px; height: 309px;
    overflow: hidden;
    box-shadow: 0 14px 30px rgba(0,0,0,0.18);
  }

  /* Back of card */
  .card--back { left: 40px; top: 250px; background: var(--navy-deep); }
  .card--back .watermark-name {
    position: absolute; left: 150px; top: 40px;
    color: var(--faint);
    font-size: 46px; font-weight: 800; line-height: 1;
    letter-spacing: 1px; text-transform: uppercase;
  }
  .card--back .brand {
    position: absolute; left: 0; right: 0; top: 100px;
    text-align: center; color: var(--white);
  }
  .brand__mark {
    display: inline-block; width: 34px; height: 34px;
    border-radius: 50%; border: 4px solid currentColor;
    margin-bottom: 10px;
  }
  .brand__name {
    font-size: 30px; font-weight: 800; letter-spacing: 1px;
    text-transform: uppercase; line-height: 1;
  }
  .brand__tagline {
    display: flex; align-items: center; justify-content: center; gap: 10px;
    margin-top: 8px;
    font-size: 18px; font-weight: 600; letter-spacing: 3px;
  }
  .brand__tagline::before, .brand__tagline::after {
    content: ""; width: 40px; height: 2px; background: currentColor;
  }

  /* Front of card */
  .card--front { left: 620px; top: 250px; background: var(--white); }
  .card--front .swoosh { position: absolute; inset: 0; }
  .card--front .brand {
    position: absolute; left: 30px; top: 46px; text-align: center;
  }
  .card--front .brand__mark { color: var(--navy); width: 26px; height: 26px; border-width: 3px; margin-bottom: 6px; }
  .card--front .brand__name { color: var(--red); font-size: 21px; }
  .card--front .brand__tagline { color: var(--navy); font-size: 13px; letter-spacing: 2px; }
  .card--front .brand__tagline::before, .card--front .brand__tagline::after { width: 22px; }

  .contact {
    position: absolute; left: 300px; top: 190px;
    color: var(--white); list-style: none;
    font-size: 12.5px; line-height: 1.35;
  }
  .contact__name {
    font-size: 15px; letter-spacing: 1.5px; text-transform: uppercase;
    display: flex; align-items: center; gap: 6px; margin-bottom: 3px;
  }
  .contact__rows { border-left: 1.5px solid var(--white); padding-left: 8px; margin-left: 5px; }
  .contact__row { display: flex; gap: 6px; align-items: flex-start; }
  .contact__row svg { flex: none; margin-top: 3px; }
  .contact__web { text-transform: uppercase; font-size: 11px; letter-spacing: 0.5px; }

  /* Standalone lockup */
  .lockup {
    position: absolute; right: 70px; top: 800px; text-align: center;
  }
  .lockup .brand__mark { color: var(--navy); }
  .lockup .brand__name { color: var(--red); font-size: 32px; }
  .lockup .brand__tagline { color: var(--navy); font-size: 19px; }
</style>
</head>
<body>
<main class="canvas">

  <section class="card card--back" aria-label="Card back">
    <div class="watermark-name" aria-hidden="true">Copper Gavel<br>Auctions</div>
    <div class="brand">
      <span class="brand__mark"></span>
      <div class="brand__name">Copper Gavel Auctions</div>
      <div class="brand__tagline">BUY-SELL-CONSIGN</div>
    </div>
  </section>

  <section class="card card--front" aria-label="Card front">
    <svg class="swoosh" viewBox="0 0 540 309" width="540" height="309" aria-hidden="true">
      <path d="M0,190 Q322,176 458,0 L540,0 L540,309 L0,309 Z" fill="var(--red)"/>
      <path d="M0,210 Q340,196 476,0 L540,0 L540,309 L0,309 Z" fill="var(--navy)"/>
    </svg>
    <div class="brand">
      <span class="brand__mark"></span>
      <div class="brand__name">Copper Gavel Auctions</div>
      <div class="brand__tagline">BUY-SELL-CONSIGN</div>
    </div>
    <div class="contact">
      <div class="contact__name">
        <svg width="12" height="12" viewBox="0 0 24 24"><path fill="#fff" d="M12 2l3 7h7l-5.5 4.5 2 7.5-6.5-4.5-6.5 4.5 2-7.5L2 9h7z"/></svg>
        Gregory Vandale
      </div>
      <div class="contact__rows">
        <div class="contact__row">
          <svg width="9" height="12" viewBox="0 0 12 16"><path fill="#5aa9e6" d="M6 0a6 6 0 0 1 6 6c0 4-6 10-6 10S0 10 0 6a6 6 0 0 1 6-6zm0 3.5a2.5 2.5 0 1 0 0 5 2.5 2.5 0 0 0 0-5z"/></svg>
          <span>482 Thornbury Road Suite<br>214C Marlow Falls NY 14583</span>
        </div>
        <div class="contact__row">
          <svg width="11" height="9" viewBox="0 0 16 12"><rect width="16" height="12" rx="1" fill="#5aa9e6"/><path d="M1 1l7 6 7-6" stroke="#1f4a80" stroke-width="1.5" fill="none"/></svg>
          <span class="contact__web">Coppergavelbids.net</span>
        </div>
        <div class="contact__row">
          <svg width="10" height="10" viewBox="0 0 16 16"><path fill="#5aa9e6" d="M3 1l3 3-2 2c1 2 4 5 6 6l2-2 3 3-2 2C7 15 1 9 1 3z"/></svg>
          <span>(555)482-6613</span>
        </div>
      </div>
    </div>
  </section>

  <div class="lockup brand">
    <span class="brand__mark"></span>
    <div class="brand__name">Copper Gavel Auctions</div>
    <div class="brand__tagline">BUY-SELL-CONSIGN</div>
  </div>

</main>
</body>
</html>
```